Flyer design 3-part folding flyer

A template for a 3-fold print flyer is to be created.

The flyer should be professional and customer-oriented as an advertising flyer that leads to the purchase of the consulting service.

The structure is an example and can be customized.
The topics are as follows:
Create a 3-part folded flyer:
🧠 Flyer design: KRVO Lieferkettenberatung GmbH
🎨 Color scheme
Orange: Energy, innovation, attention
White: Clarity, trust
Anthracite: seriousness, stability

πŸ”Ά Front (Panel 1 – Title Page)
Title: From Chaos to Clarity – AI in Your Supply Chain
Image idea: An entrepreneur with a desperate look in front of a mountain of documents and storage chaos (horror of horrors) – next to it a signpost towards the β€œBeach of Bliss” with the logo of KRVO Lieferkettenberatung GmbH.
Slogan: KRVO gets your supply chain on track – with artificial intelligence.

πŸ”Ά Inside (Panel 2 – Problem & Solution)
Headline: The challenges of modern supply chains
Key points (problem):
Overcrowded warehouses & capital tie-up
Unclear demand planning
Supply bottlenecks & production stoppages
Intransparent material flow
Errors that are detected too late
Headline Solution: Our AI solutions – your competitive advantages
Key points (solution):
βœ… Inventory reduction through intelligent forecasts
βœ… Optimized planning with real-time data
βœ… Delivery security through smart algorithms
βœ… Material flow optimization with AI
βœ… Real-time error detection and resolution

πŸ”Ά Back (Panel 3 – Call to Action & Contact)
Headline: Your path to the beach of bliss begins here.
Text: Say goodbye to the horror of horror in your supply chain.
KRVO Lieferkettenberatung GmbH: Experience meets AI – we transform your supply chain from chaos to success. Fast. Precise. Powerful in implementation. πŸš€

Call to Action: πŸ“ž Get a non-binding consultation now +49 000 1234567 🌐 www.krvo-beratung.example βœ‰οΈ kontakt@krvo-beratung.example πŸ“ Location: KRVO Lieferkettenberatung GmbH, Musterweg 1, D-00000 Musterstadt

Logo & Design: KRVO logo positioned at the bottom right, with an orange, white, and anthracite frame and clear typography.

------------------------
If you have any questions or concerns, please contact me.

```html
<!DOCTYPE html>
<html lang="en">
<head>
<meta charset="utf-8">
<title>KRVO Lieferkettenberatung – Tri-fold Flyer</title>
<link href="https://fonts.googleapis.com/css2?family=Montserrat:wght@500;700;800&family=Open+Sans:wght@400;600;700&display=swap" rel="stylesheet">
<style>
:root{
  --orange:#f39200;
  --anthracite:#2f3337;
  --grey-text:#555a5f;
  --white:#ffffff;
  --canvas:#e9e9e9;
  --photo-a:#a9a39a;
  --photo-b:#6f6a64;
  --photo-c:#c9c2b6;
}
*{box-sizing:border-box;margin:0;padding:0}
html,body{width:1200px;height:3000px;overflow:hidden;background:var(--canvas)}
body{font-family:"Open Sans",Arial,sans-serif;color:var(--anthracite);position:relative}
.spread{position:absolute;left:60px;width:1080px;height:764px;display:flex;background:var(--white);box-shadow:0 10px 30px rgba(0,0,0,.12)}
.spread--outside{top:420px}
.spread--german{top:1560px}
.panel{width:360px;height:100%;position:relative;overflow:hidden;border-right:1px solid #eee}
.panel:last-child{border-right:none}
.pad{padding:30px 28px}
.heading{font-family:"Montserrat",Arial,sans-serif;font-weight:800;line-height:1.15}
.heading--orange{color:var(--orange);font-size:19px;margin-bottom:16px}
.list{list-style:none}
.list li{display:flex;align-items:center;gap:12px;font-size:12.5px;line-height:1.35;margin-bottom:13px;color:var(--grey-text)}
.icon{flex:0 0 26px;width:26px;height:26px}
.photo{width:100%;background:linear-gradient(135deg,var(--photo-c),var(--photo-a) 55%,var(--photo-b))}
.wordmark{font-family:"Montserrat",Arial,sans-serif;font-weight:800;font-size:30px;color:var(--white);letter-spacing:1px;line-height:1}
/* outside middle */
.cta-top{background:var(--orange);padding:26px 28px 24px;color:var(--white)}
.cta-top .heading{font-size:19px;margin:20px 0 10px;text-transform:uppercase}
.cta-top p{font-size:12px;line-height:1.45}
.cta-body{padding:18px 28px;text-align:center}
.cta-body p{font-size:11.5px;line-height:1.5;color:var(--grey-text)}
.social{display:flex;justify-content:center;gap:10px;margin:14px 0}
.social span{width:26px;height:26px;border-radius:50%;background:var(--anthracite)}
.phone{font-family:"Montserrat",Arial,sans-serif;font-weight:800;font-size:20px;color:var(--orange);margin-bottom:6px}
.contact-line{font-size:11.5px;color:var(--anthracite);line-height:1.55}
.cta-photo{position:absolute;left:0;bottom:0;height:220px}
/* outside cover */
.cover-title{padding:26px 28px 0}
.cover-title .heading{font-size:30px;text-transform:uppercase}
.cover-title .heading span{display:block;color:var(--orange)}
.cover-title p{font-size:12.5px;line-height:1.5;margin-top:12px;color:var(--grey-text)}
.cover-foot{position:absolute;left:0;bottom:0;width:100%;height:120px;background:var(--orange);padding:44px 28px}
/* german */
.steps-top{background:var(--orange);color:var(--white);padding:30px 28px 22px}
.steps-top .heading{font-size:24px;margin-bottom:12px}
.steps-top p{font-size:12px;line-height:1.5}
.steps{padding:20px 28px}
.steps .heading{font-size:18px;margin-bottom:14px}
.step{display:flex;gap:12px;margin-bottom:14px}
.step__num{flex:0 0 32px;height:32px;border-radius:50%;background:var(--orange);color:var(--white);font-family:"Montserrat",Arial,sans-serif;font-weight:800;font-size:16px;display:flex;align-items:center;justify-content:center}
.step strong{display:block;font-family:"Montserrat",Arial,sans-serif;font-size:15px}
.step small{font-size:11.5px;color:var(--grey-text)}
.title-de{padding:32px 28px 16px}
.title-de .heading{font-size:32px}
.title-de .heading span{color:var(--orange)}
.title-de p{font-size:13px;line-height:1.5;margin-top:12px;color:var(--grey-text)}
.de-foot{position:absolute;left:0;bottom:0;width:100%;height:170px;background:var(--orange);padding:44px 28px}
.de-foot .url{position:absolute;bottom:18px;right:28px;font-size:11px;color:var(--white)}
</style>
</head>
<body>
<svg width="0" height="0" style="position:absolute">
  <symbol id="i-warn" viewBox="0 0 26 26"><circle cx="13" cy="13" r="12" fill="none" stroke="#f39200" stroke-width="1.6"/><path d="M13 7v8M13 18v1.5" stroke="#f39200" stroke-width="2.2" stroke-linecap="round"/></symbol>
  <symbol id="i-tick" viewBox="0 0 26 26"><circle cx="13" cy="13" r="12" fill="#f39200"/><path d="M7.5 13.5l3.7 3.7 7.3-7.5" fill="none" stroke="#fff" stroke-width="2.4" stroke-linecap="round" stroke-linejoin="round"/></symbol>
</svg>

<section class="spread spread--outside">
  <div class="panel pad">
    <h2 class="heading heading--orange">The challenges of modern supply chains (problem)</h2>
    <ul class="list">
      <li><svg class="icon"><use href="#i-warn"/></svg>Overcrowded warehouses &amp; capital tie-up</li>
      <li><svg class="icon"><use href="#i-warn"/></svg>Unclear demand planning</li>
      <li><svg class="icon"><use href="#i-warn"/></svg>Supply bottlenecks &amp; production stoppages</li>
      <li><svg class="icon"><use href="#i-warn"/></svg>Intransparent material flow</li>
      <li><svg class="icon"><use href="#i-warn"/></svg>Errors that are detected too late</li>
    </ul>
    <h2 class="heading heading--orange" style="margin-top:26px">Our AI solutions – your competitive advantages (solution)</h2>
    <ul class="list">
      <li><svg class="icon"><use href="#i-tick"/></svg>Inventory reduction through intelligent forecasts</li>
      <li><svg class="icon"><use href="#i-tick"/></svg>Optimized planning with real-time data</li>
      <li><svg class="icon"><use href="#i-tick"/></svg>Delivery security through smart algorithms</li>
      <li><svg class="icon"><use href="#i-tick"/></svg>Material flow optimization with AI</li>
      <li><svg class="icon"><use href="#i-tick"/></svg>Real-time error detection and resolution</li>
    </ul>
  </div>

  <div class="panel">
    <div class="cta-top">
      <div class="wordmark">KRVO</div>
      <h2 class="heading">Your path to the beach of bliss begins here</h2>
      <p>Say goodbye to the horror of horror in your supply chain.</p>
    </div>
    <div class="cta-body">
      <p>KRVO Lieferkettenberatung GmbH: Experience meets AI – we transform your supply chain from chaos to success. Fast. Precise. Powerful in implementation.</p>
      <div class="social"><span></span><span></span><span></span><span></span></div>
      <div class="phone">+49 000 1234567</div>
      <div class="contact-line">www.krvo-beratung.example</div>
      <div class="contact-line">kontakt@krvo-beratung.example</div>
      <div class="contact-line">KRVO Lieferkettenberatung GmbH</div>
      <div class="contact-line">Musterweg 1, D-00000 Musterstadt</div>
    </div>
    <div class="photo cta-photo" role="img" aria-label="Photo of a consulting team meeting around a table"></div>
  </div>

  <div class="panel">
    <div class="photo" style="height:330px" role="img" aria-label="Photo of a desperate entrepreneur in front of piles of documents, with a signpost to the Beach of Bliss"></div>
    <div class="cover-title">
      <h1 class="heading">From chaos to clarity<span>AI in your supply chain</span></h1>
      <p>KRVO gets your supply chain on track – with artificial intelligence.</p>
    </div>
    <div class="cover-foot">
      <div class="wordmark">KRVO</div>
    </div>
  </div>
</section>

<section class="spread spread--german" lang="de">
  <div class="panel">
    <div class="photo" style="height:190px" role="img" aria-label="Foto von Geschäftsleuten bei der Analyse von Unterlagen"></div>
    <div class="pad" style="padding-top:22px">
      <h2 class="heading heading--orange" style="font-size:21px">Probleme in der Supply Chain?</h2>
      <ul class="list">
        <li><svg class="icon"><use href="#i-warn"/></svg>Hohe Lagerkosten</li>
        <li><svg class="icon"><use href="#i-warn"/></svg>Hohe Operativkosten</li>
        <li><svg class="icon"><use href="#i-warn"/></svg>Steigende Lieferzeiten</li>
      </ul>
      <h2 class="heading heading--orange" style="font-size:21px;margin-top:18px">Unsere Leistungen</h2>
      <ul class="list">
        <li><svg class="icon"><use href="#i-tick"/></svg>Identifizierung kostenrelevanter Faktoren</li>
        <li><svg class="icon"><use href="#i-tick"/></svg>Präzisere Bestandsplanung</li>
      </ul>
    </div>
  </div>

  <div class="panel">
    <div class="steps-top">
      <h2 class="heading">Ihre Lieferkette auf dem Prüfstand?</h2>
      <p>KRVO hilft mittelständischen Unternehmen, Lagerbestände zu senken, Engpässe früh zu erkennen und Abläufe mit künstlicher Intelligenz messbar zu verbessern.</p>
    </div>
    <div class="steps">
      <h3 class="heading">Wie wir vorgehen</h3>
      <div class="step"><div class="step__num">1</div><div><strong>Analyse</strong><small>Wir prüfen Ihre Daten und Prozesse.</small></div></div>
      <div class="step"><div class="step__num">2</div><div><strong>Empfehlungen</strong><small>Konkrete Maßnahmen mit klarem Nutzen.</small></div></div>
      <div class="step"><div class="step__num">3</div><div><strong>Implementieren</strong><small>Umsetzung gemeinsam mit Ihrem Team.</small></div></div>
    </div>
    <div class="photo cta-photo" style="height:200px" role="img" aria-label="Foto eines Beratungsgesprächs im Büro"></div>
  </div>

  <div class="panel">
    <div class="title-de">
      <h1 class="heading">KI für eine starke <span>Lieferkette</span></h1>
      <p>Optimieren Sie Ihre Supply Chain mit Künstlicher Intelligenz</p>
    </div>
    <div class="photo" style="height:250px" role="img" aria-label="Foto eines Lagers mit Regalen und Warenpaletten"></div>
    <div class="de-foot">
      <div class="wordmark">KRVO</div>
      <div class="url">www.krvo-beratung.example</div>
    </div>
  </div>
</section>
</body>
</html>
```